Business Card Design for Irrigation Contractor

Design and layout for company business cards to include the following information:
1. Logo
2. Installation \ Service \ Maintenance
3. U-47283
4. Walter J. Lindqvist
5. walter@7Kirrigation.com
6. Office 555-712-9364
7. Cell 555-286-0517

```html
<!DOCTYPE html>
<html lang="en">
<head>
<meta charset="utf-8">
<title>7K Irrigation – Business Cards</title>
<link href="https://fonts.googleapis.com/css2?family=Montserrat:wght@400;500;700;800&display=swap" rel="stylesheet">
<style>
  :root {
    --navy: #13294b;
    --navy-mid: #1f4d7a;
    --blue: #3f9ad2;
    --sky: #5bbdec;
    --white: #ffffff;
    --muted: #3a4a63;
    --stage: #2b2d31;
  }
  * { box-sizing: border-box; margin: 0; padding: 0; }
  html, body { width: 1200px; height: 900px; overflow: hidden; }
  body {
    background: var(--stage);
    font-family: "Montserrat", Arial, sans-serif;
    position: relative;
  }
  .card {
    position: absolute;
    left: 250px;
    width: 700px;
    height: 400px;
    border-radius: 22px;
    overflow: hidden;
    box-shadow: 0 10px 30px rgba(0,0,0,.45);
  }
  /* ---------- front ---------- */
  .card-front {
    top: 30px;
    background: linear-gradient(35deg, var(--sky) 0%, var(--blue) 40%, var(--navy-mid) 85%, #1b3d63 100%);
    color: var(--white);
  }
  .front-deco {
    position: absolute;
    right: -60px;
    top: -40px;
    width: 340px;
    height: 340px;
    border-radius: 50%;
    background: rgba(255,255,255,.06);
  }
  .front-brand {
    position: absolute;
    left: 0; right: 0;
    top: 140px;
    display: flex;
    align-items: center;
    justify-content: center;
    gap: 18px;
  }
  .brand-dot {
    width: 60px; height: 60px;
    border-radius: 50%;
    background: var(--white);
  }
  .front-brand .brand-name {
    font-size: 56px;
    font-weight: 800;
    letter-spacing: 1px;
    color: var(--white);
  }
  .front-tagline {
    position: absolute;
    left: 0; right: 0;
    top: 230px;
    text-align: center;
    font-size: 20px;
    font-weight: 500;
    letter-spacing: 1px;
  }
  .front-tagline span + span::before { content: "•"; margin: 0 14px; }
  .front-tagline span:first-child::before { content: "•"; margin-right: 8px; }

  /* ---------- back ---------- */
  .card-back {
    top: 470px;
    background: var(--white);
  }
  .back-waves { position: absolute; inset: 0; }
  .back-brand {
    position: absolute;
    left: 40px;
    top: 132px;
    display: flex;
    align-items: center;
    gap: 14px;
  }
  .back-brand .brand-dot { background: var(--blue); width: 50px; height: 50px; }
  .back-brand .brand-name {
    font-size: 40px;
    font-weight: 800;
    color: var(--navy);
  }
  .person {
    position: absolute;
    right: 40px;
    top: 20px;
    text-align: right;
    color: var(--navy);
  }
  .person-name { font-size: 26px; font-weight: 800; }
  .person-title { font-size: 15px; font-weight: 500; margin-top: 2px; }
  .person-license { font-size: 13px; font-weight: 400; margin-top: 2px; color: var(--muted); }
  .contacts {
    position: absolute;
    right: 30px;
    top: 228px;
    list-style: none;
    color: var(--white);
  }
  .contacts li {
    display: flex;
    align-items: center;
    justify-content: flex-end;
    gap: 12px;
    font-size: 16px;
    height: 34px;
  }
  .contact-icon {
    width: 26px; height: 26px;
    border-radius: 6px;
    background: var(--white);
    display: flex; align-items: center; justify-content: center;
  }
</style>
</head>
<body>

<section class="card card-front" aria-label="Business card front">
  <div class="front-deco"></div>
  <div class="front-brand">
    <div class="brand-dot"></div>
    <div class="brand-name">7K IRRIGATION</div>
  </div>
  <p class="front-tagline"><span>Installation</span><span>Service</span><span>Maintenance</span></p>
</section>

<section class="card card-back" aria-label="Business card back">
  <svg class="back-waves" viewBox="0 0 700 400" width="700" height="400" aria-hidden="true">
    <defs>
      <linearGradient id="waveNavy" x1="1" y1="0" x2="0.2" y2="1">
        <stop offset="0" stop-color="#13294b"/>
        <stop offset="0.5" stop-color="#24578a"/>
        <stop offset="1" stop-color="#4aa8dc"/>
      </linearGradient>
    </defs>
    <path d="M700,122 C610,122 530,157 470,202 C400,257 330,335 0,372 L0,400 L700,400 Z" fill="url(#waveNavy)"/>
    <path d="M700,108 C600,108 520,145 460,190 C430,212 412,230 398,243" fill="none" stroke="#1b3d63" stroke-width="4"/>
    <path d="M0,322 C170,338 300,300 400,240 C320,305 200,350 0,348 Z" fill="#5bbdec"/>
    <path d="M80,392 C250,380 360,330 430,270" fill="none" stroke="#ffffff" stroke-width="3"/>
  </svg>

  <div class="back-brand">
    <div class="brand-dot"></div>
    <div class="brand-name">7K IRRIGATION</div>
  </div>

  <div class="person">
    <div class="person-name">Walter J. Lindqvist</div>
    <div class="person-title">Managing Director</div>
    <div class="person-license">U-47283</div>
  </div>

  <ul class="contacts">
    <li>555-712-9364 (Office)
      <span class="contact-icon"><svg width="14" height="16" viewBox="0 0 14 16"><rect x="2" y="0.5" width="10" height="15" rx="2" fill="none" stroke="#13294b" stroke-width="1.6"/><circle cx="7" cy="12.5" r="1" fill="#13294b"/></svg></span></li>
    <li>555-286-0517
      <span class="contact-icon"><svg width="16" height="14" viewBox="0 0 16 14"><path d="M1,5 C4,1 12,1 15,5 L13,7 L11,5 L5,5 L3,7 Z" fill="#13294b"/><rect x="3" y="7" width="10" height="6" rx="1" fill="#13294b"/></svg></span></li>
    <li>walter@7Kirrigation.com
      <span class="contact-icon"><svg width="16" height="12" viewBox="0 0 16 12"><rect x="0.5" y="0.5" width="15" height="11" fill="#13294b"/><path d="M1,1 L8,7 L15,1" fill="none" stroke="#fff" stroke-width="1.3"/></svg></span></li>
    <li>www.7Kirrigation.com
      <span class="contact-icon"><svg width="16" height="16" viewBox="0 0 16 16"><circle cx="8" cy="8" r="7" fill="none" stroke="#13294b" stroke-width="1.6"/><ellipse cx="8" cy="8" rx="3" ry="7" fill="none" stroke="#13294b" stroke-width="1.2"/><line x1="1" y1="8" x2="15" y2="8" stroke="#13294b" stroke-width="1.2"/></svg></span></li>
  </ul>
</section>

</body>
</html>
```